(EXPEDITE)Marketing Collateral For 'Radiant Occasion Hosts' | ||
Brochures & Postcards | ||
Double-sided Postcards 8.5 X 5.5 | Any style Brochure | "Having an outstanding track record of successfully designing dream weddings, as well as providing management services to stage productions, our multi-specialists provide it all. From perfect wedding locations to imaginative themes, invitations, decorations, catering and logistics, we take care of every detail to make your event a stress-free, seamlessly managed occasion for everyone to enjoy." *Content (writing) for the Postcards and Brochures will be given soon, please fill in "text here" spaces until then |
Events | ||
Upper Class, Corporate, Brides & Grooms, Weddings, Sweet Sixteens, Private Parties | ||
Use a minimum of 6 pictures from our 'Radiant Occasion Hosts' company that have been uploaded Additional pictures can be downloaded from the following link: http://qxvlo.example/k3maTeLp9Wudra |

```html
<!DOCTYPE html>
<html lang="en">
<head>
<meta charset="utf-8">
<title>Radiant Occasion Hosts – Brochure &amp; Postcard</title>
<link href="https://fonts.googleapis.com/css2?family=Open+Sans:wght@400;600;700&display=swap" rel="stylesheet">
<style>
:root{
  --stage:#3b3b3b;
  --paper:#ffffff;
  --plum:#4a1242;
  --wine:#6d1c5f;
  --magenta:#a3207f;
  --orchid:#d65cc0;
  --blush:#f7d3ef;
  --gold:#c9a24a;
  --ink:#333333;
  --muted:#777777;
  --label:#ffffff;
}
*{box-sizing:border-box;margin:0;padding:0}
html,body{width:1200px;height:1014px;overflow:hidden;background:var(--stage)}
body{position:relative;font-family:"Open Sans",Arial,sans-serif;color:var(--ink)}
.label{position:absolute;color:var(--label);font-weight:600;font-size:19px;width:201px;text-align:center}
.photo{position:absolute}
.photo--party{background:
  linear-gradient(180deg,rgba(74,18,66,0) 55%,rgba(255,214,150,.55) 88%,rgba(74,18,66,.7) 100%),
  radial-gradient(ellipse at 50% 30%,var(--blush) 0%,var(--orchid) 30%,var(--magenta) 60%,var(--plum) 100%)}
.photo--reception{background:
  linear-gradient(180deg,var(--plum) 0%,var(--wine) 40%,var(--magenta) 65%,#e9b6d9 85%,#f3e6c8 100%)}
.photo--hall{background:
  linear-gradient(180deg,#caa4d8 0%,#e8d8ef 40%,#b77fc6 70%,#5b2a67 100%)}
.photo--cake{background:
  radial-gradient(ellipse at 50% 55%,#ffffff 0%,#f1e6ef 30%,#c49bbe 62%,#6a3a66 100%)}

/* brochure */
.brochure{position:absolute;left:520px;width:603px;display:flex}
.brochure--outside{top:49px;height:439px}
.brochure--inside{top:548px;height:444px;border-left:3px solid var(--gold)}
.panel{position:relative;width:201px;height:100%;background:var(--paper);overflow:hidden}
.panel--back{background:linear-gradient(180deg,var(--wine) 0%,var(--magenta) 45%,var(--wine) 100%)}
.copy{padding:12px 12px 0}
.copy h3{font-size:8px;font-weight:700;margin-bottom:5px}
.copy p{font-size:6px;line-height:1.5;color:var(--muted);margin-bottom:8px}
.brand{font-weight:600;color:var(--paper);text-align:center;line-height:1.15}
.back-band{position:absolute;left:0;right:0;top:300px;bottom:0;background:var(--wine)}
.back-brand{position:absolute;left:0;right:0;top:330px;font-size:18px;display:flex;align-items:center;justify-content:center;gap:8px}
.back-brand .dot{width:12px;height:12px;border-radius:50%;background:var(--paper);flex:none}
.back-web{position:absolute;left:0;right:0;top:404px;text-align:center;color:var(--paper);font-size:10px;font-weight:600}
.front-badge{position:absolute;left:22px;right:22px;top:26px;height:118px;border-radius:50%;background:var(--paper);border:3px solid var(--gold);display:flex;align-items:center;justify-content:center}
.front-badge .brand{color:var(--magenta);font-size:17px}
.inside-top{position:absolute;top:0;left:0;right:0;height:118px}
.inside-photos{position:absolute;top:118px;left:0;right:0;height:196px}
.inside-lower{position:absolute;top:314px;left:0;right:0}

/* postcards */
.postcard{position:absolute;left:96px;width:330px;background:var(--paper)}
.postcard--front{top:252px;height:214px}
.postcard--back{top:488px;height:219px}
.pc-text{position:absolute;left:266px;top:90px;font-size:7px;color:var(--ink)}
.pc-brand{position:absolute;left:236px;bottom:22px;width:94px;font-size:9px;font-weight:600;color:var(--magenta);text-align:center;line-height:1.2}
.pc-web{position:absolute;left:18px;top:14px;font-size:13px;color:var(--ink)}
.pc-web b{font-weight:700}
.stamp{position:absolute;right:40px;top:16px;width:38px;height:38px;border:1px solid #bbbbbb;background:#d9d9d9}
.address-lines{position:absolute;left:196px;top:76px;width:120px}
.address-lines span{display:block;height:1px;background:var(--gold);margin-bottom:13px}
.pc-contact{position:absolute;left:18px;bottom:12px;font-size:6px;line-height:1.6;color:var(--muted)}
.pc-contact b{color:var(--ink)}
</style>
</head>
<body>

<div class="label" style="left:520px;top:14px">Inside Fold</div>
<div class="label" style="left:721px;top:14px">Back</div>
<div class="label" style="left:922px;top:14px">Front</div>

<section class="brochure brochure--outside">
  <article class="panel panel--fold">
    <div class="copy">
      <h3>About Us</h3>
      <p>We plan weddings, galas and private parties with care, from venue and theme to catering and logistics, so every guest can relax.</p>
      <p>We plan weddings, galas and private parties with care, from venue and theme to catering and logistics, so every guest can relax.</p>
      <p>We plan weddings, galas and private parties with care, from venue and theme to catering and logistics, so every guest can relax.</p>
      <p>We plan weddings, galas and private parties with care, from venue and theme to catering and logistics, so every guest can relax.</p>
    </div>
    <div class="photo photo--reception" style="left:0;right:0;top:329px;bottom:0" role="img" aria-label="Photo of a purple-lit reception hall with a dance floor"></div>
  </article>
  <article class="panel panel--back">
    <div class="back-band"></div>
    <div class="brand back-brand"><span class="dot"></span><span>Radiant Occasion<br>Hosts</span></div>
    <div class="back-web">www.website.com</div>
  </article>
  <article class="panel panel--front">
    <div class="photo photo--party" style="inset:0" role="img" aria-label="Photo of a floral centrepiece with candles under purple light"></div>
    <div class="front-badge"><div class="brand">Radiant Occasion<br>Hosts</div></div>
  </article>
</section>

<div class="label" style="left:520px;top:508px">Inside 1</div>
<div class="label" style="left:721px;top:508px">Inside 2</div>
<div class="label" style="left:922px;top:508px">Inside 3</div>

<section class="brochure brochure--inside">
  <article class="panel">
    <div class="copy inside-top">
      <h3>Title</h3>
      <p>Elegant décor, fine catering and seamless timing shaped around your vision and your guests.</p>
      <p>Elegant décor, fine catering and seamless timing shaped around your vision and your guests.</p>
    </div>
    <div class="photo photo--party inside-photos" role="img" aria-label="Photo of candles and flowers on a reception table"></div>
    <div class="copy inside-lower">
      <h3>Title</h3>
      <p>Elegant décor, fine catering and seamless timing shaped around your vision and your guests.</p>
      <p>Elegant décor, fine catering and seamless timing shaped around your vision and your guests.</p>
    </div>
  </article>
  <article class="panel">
    <div class="copy inside-top">
      <h3>Title</h3>
      <p>Elegant décor, fine catering and seamless timing shaped around your vision and your guests.</p>
      <p>Elegant décor, fine catering and seamless timing shaped around your vision and your guests.</p>
    </div>
    <div class="photo photo--cake inside-photos" role="img" aria-label="Photo of a tiered white wedding cake"></div>
    <div class="copy inside-lower">
      <h3>Title</h3>
      <p>Elegant décor, fine catering and seamless timing shaped around your vision and your guests.</p>
      <p>Elegant décor, fine catering and seamless timing shaped around your vision and your guests.</p>
    </div>
  </article>
  <article class="panel">
    <div class="copy inside-top">
      <h3>Title</h3>
      <p>Elegant décor, fine catering and seamless timing shaped around your vision and your guests.</p>
      <p>Elegant décor, fine catering and seamless timing shaped around your vision and your guests.</p>
    </div>
    <div class="photo photo--hall inside-photos" role="img" aria-label="Photo of a ballroom set with round tables and lilac lighting"></div>
    <div class="copy inside-lower">
      <h3>Title</h3>
      <p>Elegant décor, fine catering and seamless timing shaped around your vision and your guests.</p>
      <p>Elegant décor, fine catering and seamless timing shaped around your vision and your guests.</p>
    </div>
  </article>
</section>

<section class="postcard postcard--front">
  <div class="photo photo--party" style="left:0;top:0;bottom:0;width:228px" role="img" aria-label="Photo of a candlelit floral table setting in purple light"></div>
  <div class="pc-text">Text Here</div>
  <div class="pc-brand">Radiant Occasion Hosts</div>
</section>

<section class="postcard postcard--back">
  <div class="pc-web"><b>www.</b>website<b>.com</b></div>
  <div class="stamp"></div>
  <div class="address-lines"><span></span><span></span><span></span><span></span><span></span></div>
  <div class="pc-contact">
    <b>Address :</b> 120 Linden Avenue, Suite 4<br>
    <b>Phone :</b> 555 0142 318<br>
    <b>Email :</b> hello@radiantoccasion.example
  </div>
</section>

</body>
</html>
```